New Stationary for our business

We are a gift business and would like to create a new corporate image with new stationary and design.

We would like a Classic Corporate look with a touch of Flair.

We would need:
Envelopes
Letter Head
Business Cards
With Comp Slips
Note Pads
Etc...

Our details are:

Basket Haven Pty Ltd
518 Tallow Street, Fernmead, Victoria, 3071
1800 742 918
www.baskethaven-demo.com.au
sales@baskethaven-demo.com.au

ABN: 58 603 214 796

Target Market(s)

Corporate Look

Industry/Entity Type

Marketing

Contact Information for Business Card

Basket Haven Pty Ltd
1800 742 918
518 Tallow Street
Fernmead 3071
Victoria Australia

Darren Pelluso - Managing Director
darren.pelluso@baskethaven-demo.com.au
0413 587 120

Logo Text

Basket Haven - The Gift Specialists

Colors

Designer to choose colors to be used in the design.

Requirements
Must have
• Look and Feel upmarket and exclusive

```html
<!DOCTYPE html>
<html lang="en">
<head>
<meta charset="utf-8">
<title>Basket Haven — Stationery Suite</title>
<link href="https://fonts.googleapis.com/css2?family=Josefin+Slab:wght@400;600&family=Josefin+Sans:wght@400&family=Tinos&family=Great+Vibes&display=swap" rel="stylesheet">
<style>
  :root{
    --bg:#d8d8d8;
    --paper:#ffffff;
    --paper-soft:#f4f4f4;
    --ink:#1b1b1b;
    --ink-soft:#3a3a3a;
    --black:#141414;
    --black-2:#262626;
    --gold:#c9a43a;
    --gold-light:#f3dc72;
    --gold-deep:#c8a02a;
    --signature:#4a68a8;
    --shadow:0 2px 6px rgba(0,0,0,.18);
  }
  *{box-sizing:border-box;margin:0;padding:0}
  html,body{width:1200px;height:794px;overflow:hidden}
  body{background:var(--bg);position:relative;font-family:"Josefin Slab",serif;color:var(--ink)}
  .piece{position:absolute;box-shadow:var(--shadow)}
  .wordmark{font-family:"Josefin Slab",serif;font-weight:600;letter-spacing:.04em;text-transform:uppercase;white-space:nowrap;text-align:center}

  /* Letterhead */
  .letterhead{left:46px;top:132px;width:342px;height:486px;background:var(--paper)}
  .letterhead .wordmark{position:absolute;left:0;right:0;top:58px;font-size:19px;color:var(--ink)}
  .letter-greeting{position:absolute;left:40px;top:154px;font-family:"Josefin Sans",sans-serif;font-size:10.5px}
  .letter-body{position:absolute;left:40px;width:260px;font-family:"Josefin Sans",sans-serif;font-size:5.8px;line-height:7.6px;color:var(--ink-soft)}
  .letter-body.p1{top:186px}.letter-body.p2{top:242px}.letter-body.p3{top:290px}
  .letter-closing{position:absolute;right:42px;top:362px;font-family:"Josefin Sans",sans-serif;font-size:6px}
  .letter-signature{position:absolute;right:42px;top:380px;font-family:"Great Vibes",cursive;font-size:16px;color:var(--signature)}
  .letter-footer-title{position:absolute;left:0;right:0;top:434px;text-align:center;font-family:"Tinos",serif;font-size:6.6px}
  .letter-footer-rule{position:absolute;left:12px;right:12px;top:443px}
  .letter-footer-text{position:absolute;left:32px;right:32px;top:452px;font-family:"Tinos",serif;font-size:5.6px;line-height:10px;display:flex;justify-content:space-between}

  /* Envelopes */
  .envelope-back{left:414px;top:122px;width:350px;height:160px;background:var(--paper-soft);overflow:hidden}
  .envelope-back svg{position:absolute;inset:0}
  .envelope-back .wordmark{position:absolute;left:0;right:0;top:30px;font-size:8.5px}
  .envelope-front{left:434px;top:212px;width:350px;height:152px;background:var(--paper)}
  .envelope-front .wordmark{position:absolute;left:10px;top:21px;font-size:8.5px}
  .envelope-address{position:absolute;left:10px;top:113px;font-size:5.4px;line-height:7.2px;color:var(--ink-soft)}

  /* Business cards */
  .card{width:185px;height:112px}
  .card.light{background:var(--paper);color:var(--ink)}
  .card.dark{background:linear-gradient(180deg,var(--black-2),var(--black));color:#ececec}
  .card-front .wordmark{position:absolute;left:0;right:0;top:49px;font-size:12px;color:var(--gold)}
  .card-back svg{position:absolute;left:0;top:0}
  .card-back .wordmark{position:absolute;left:0;right:0;top:10px;font-size:7px}
  .card.light .card-back-mark{color:var(--ink)}
  .card.dark .card-back-mark{color:#ededed}
  .card-company{position:absolute;left:0;right:0;top:41px;text-align:center;font-size:7px}
  .card-company span{border-bottom:.6px solid currentColor;padding:0 4px 1px}
  .card-details{position:absolute;left:0;right:0;top:60px;text-align:center;font-size:5.2px;line-height:7.6px}
  .card-band{position:absolute;left:0;right:0;bottom:0;height:13px;background:linear-gradient(90deg,var(--gold-deep),var(--gold-light),var(--gold-deep));text-align:center;font-size:5.2px;line-height:13px;color:#3b3010}

  /* Notebooks */
  .notebook{top:402px;width:254px;height:356px}
  .notebook.light{left:438px;background:linear-gradient(180deg,#f2f2f2,#e7e7e7)}
  .notebook.dark{left:721px;background:linear-gradient(180deg,var(--black-2),var(--black))}
  .notebook-spiral{position:absolute;left:-8px;top:12px;bottom:12px;width:18px;background:repeating-linear-gradient(180deg,#1e1e1e 0 2.4px,transparent 2.4px 9.6px)}
  .notebook .wordmark{position:absolute;left:0;right:0;top:168px;font-size:19px}
  .notebook.light .wordmark{color:var(--ink)}
  .notebook.dark .wordmark{color:var(--gold)}

  /* Gift tags */
  .tag{width:128px;height:176px;transform:rotate(15deg)}
  .tag.dark{left:992px;top:432px;background:var(--black)}
  .tag.light{left:1050px;top:586px;background:var(--paper)}
  .tag-hole{position:absolute;top:10px;left:58px;width:10px;height:10px;border-radius:50%;background:var(--bg)}
  .tag-inner{position:absolute;left:50%;top:50%;width:170px;transform:translate(-50%,-50%) rotate(-90deg);text-align:center}
  .tag .wordmark{font-size:11px}
  .tag.dark .wordmark{color:var(--gold)}
  .tag.light .wordmark{color:var(--ink)}
  .tag-greeting{font-family:"Great Vibes",cursive;font-size:11px;margin-top:8px}
  .tag.dark .tag-greeting{color:var(--gold)}
  .tag.light .tag-greeting{color:var(--ink)}
</style>
</head>
<body>

  <!-- Letterhead -->
  <section class="piece letterhead">
    <div class="wordmark">Basket Haven</div>
    <p class="letter-greeting">Dear Mr. Hollis,</p>
    <p class="letter-body p1">Lorem ipsum dolor sit amet, consectetur adipiscing elit. Donec orci purus, luctus vitae dignissim eu, iaculis sed purus. Vivamus faucibus, ipsum nec aliquet viverra, leo mauris condimentum ligula, sit amet sagittis enim ligula quis arcu. Nam egestas tortor id nisi porttitor mattis. In tortor ante, ultricies in suscipit a, tempus non massa. Vivamus et auctor mi. Fusce vel massa nulla. Phasellus nec eros mauris, et scelerisque orci.</p>
    <p class="letter-body p2">Donec malesuada orci vitae nulla accumsan porta a id massa. Quisque accumsan iaculis magna sit amet fringilla. Maecenas consequat, magna eget tincidunt semper, odio nibh rutrum mi, id feugiat ante nisi eu risus. Vestibulum nunc orci, rhoncus a placerat in, ultricies in mi. Cras mattis varius eros, vel fringilla nisi suscipit eget. Quisque scelerisque sagittis nulla at porttitor.</p>
    <p class="letter-body p3">Sed id augue vitae urna euismod commodo aliquet a quam. Pellentesque arcu velit, cursus et malesuada ut, consequat et diam. Nullam erat sem, rhoncus id ullamcorper vitae, rhoncus et arcu. In ultricies ultricies nulla, ut rutrum nisi iaculis at. Donec eu magna a metus ornare faucibus. Fusce aliquet faucibus ultricies. Morbi semper, est id tincidunt gravida, sem arcu adipiscing lacus, ac bibendum nulla leo eu purus. Quisque nec diam sed risus consectetur a cumsan quis nibh. Vestibulum id purus lorem.</p>
    <p class="letter-closing">Sincerely,</p>
    <p class="letter-signature">Owen Hale</p>
    <p class="letter-footer-title">Head Office and Retail Room</p>
    <svg class="letter-footer-rule" width="318" height="6" viewBox="0 0 318 6">
      <line x1="10" y1="3" x2="308" y2="3" stroke="#1b1b1b" stroke-width="1"/>
      <path d="M0 3 L6 0 L6 6 Z M318 3 L312 0 L312 6 Z" fill="#1b1b1b"/>
    </svg>
    <div class="letter-footer-text">
      <div>Basket Haven Pty Ltd ~ 518 Tallow Street, Fernmead VIC 3071<br>Tel: 03 9471 2280 ~ Fax: 03 9471 2281 ~ sales@baskethaven-demo.com.au</div>
      <div>ACN 603 214 796<br>ABN 58 603 214 796</div>
    </div>
  </section>

  <!-- Envelopes -->
  <section class="piece envelope-back">
    <svg width="350" height="160" viewBox="0 0 350 160">
      <path d="M0 0 L155 66 Q175 74 195 66 L350 0" fill="#fbfbfb" stroke="#dcdcdc" stroke-width="1"/>
      <path d="M0 160 L140 80 M350 160 L210 80" stroke="#e2e2e2" stroke-width="1"/>
    </svg>
    <div class="wordmark">Basket Haven</div>
  </section>
  <section class="piece envelope-front">
    <div class="wordmark">Basket Haven</div>
    <p class="envelope-address">1800 742 918<br>sales@baskethaven-demo.com.au<br>518 Tallow Street, Fernmead,<br>Victoria, 3071.</p>
  </section>

  <!-- Business cards: fronts -->
  <section class="piece card light card-front" style="left:804px;top:122px">
    <div class="wordmark">Basket Haven</div>
  </section>
  <section class="piece card dark card-front" style="left:1002px;top:122px">
    <div class="wordmark">Basket Haven</div>
  </section>

  <!-- Business cards: backs -->
  <section class="piece card light card-back" style="left:804px;top:250px">
    <svg width="185" height="30" viewBox="0 0 185 30"><polyline points="36,0 36,14 48,24 137,24 149,14 149,0" fill="none" stroke="#c9a43a" stroke-width="1.4"/></svg>
    <div class="wordmark card-back-mark">Basket Haven</div>
    <p class="card-company"><span>Basket Haven Pty Ltd</span></p>
    <p class="card-details">1800 742 918<br>sales@baskethaven-demo.com.au<br>518 Tallow Street, Fernmead,<br>Victoria, 3071.</p>
    <div class="card-band">www.baskethaven-demo.com.au</div>
  </section>
  <section class="piece card dark card-back" style="left:1002px;top:250px">
    <svg width="185" height="30" viewBox="0 0 185 30"><polyline points="36,0 36,14 48,24 137,24 149,14 149,0" fill="none" stroke="#c9a43a" stroke-width="1.4"/></svg>
    <div class="wordmark card-back-mark">Basket Haven</div>
    <p class="card-company"><span>Basket Haven Pty Ltd</span></p>
    <p class="card-details">1800 742 918<br>sales@baskethaven-demo.com.au<br>518 Tallow Street, Fernmead,<br>Victoria, 3071.</p>
    <div class="card-band">www.baskethaven-demo.com.au</div>
  </section>

  <!-- Notebooks -->
  <section class="piece notebook light">
    <div class="notebook-spiral"></div>
    <div class="wordmark">Basket Haven</div>
  </section>
  <section class="piece notebook dark">
    <div class="notebook-spiral" style="background:repeating-linear-gradient(180deg,#3a3a3a 0 2.4px,transparent 2.4px 9.6px)"></div>
    <div class="wordmark">Basket Haven</div>
  </section>

  <!-- Gift tags -->
  <section class="piece tag dark">
    <div class="tag-hole"></div>
    <div class="tag-inner">
      <div class="wordmark">Basket Haven</div>
      <p class="tag-greeting">Greetings with Love</p>
    </div>
  </section>
  <section class="piece tag light">
    <div class="tag-hole"></div>
    <div class="tag-inner">
      <div class="wordmark">Basket Haven</div>
      <p class="tag-greeting">Merry Christmas</p>
    </div>
  </section>

</body>
</html>
```